Green Logistics / Last Mile Delivery Firm needs cool one-page website

FYI - We do have a detailed brief in the uploaded files section below
COMPANY
We recently launched the company Brook Logistics which is a pioneer in urban green logistics and provides zero-emissions last mile delivery services (i.e. delivery of parcels with delivery vans to the doorstep of households) for its logistics and retail clients.
We take on urban parcel delivery for our clients with a 100% electric commercial vehicles fleet, fair and sustainable working conditions for our employees and an unparalleled professional and customer-focused mindset.
WEBSITE
In the detailed brief, we have provided examples to emulate. We need the design + coding of the website. Website needs to be friendly/optimized for and should open swiftly on both Android & iOS.
In general, the website should convey
- green mission of the company
- sustainability (good working conditions, focus on employees)
- customer orientation
- professionalism
DESIGN
In the detailed brief, we have provided designs to emulate.
Color design: we do have a logo which features 2 green colors (one lighter and one darker color tone). However, the colors on the website do not necessarily need to follow these 2 colors exactly as we are able to switch the logo colors.
Imagery: should reflect maybe 50% green/leaf/tree , 25% customer and employee orientation, and 25% logistics (here it's important that it is the last mile delivery, i.e. delivery with delivery vans to the doorstep of households)
Coding

```html
<!DOCTYPE html>
<html lang="en">
<head>
<meta charset="utf-8">
<title>Brook Logistics — Sustainable Last Mile</title>
<link rel="stylesheet" href="https://fonts.googleapis.com/css2?family=Barlow+Condensed:wght@500;600&family=Montserrat:wght@400;500;600&family=Roboto:wght@400;500&display=swap">
<style>
:root{
  --green-dark:#1f8f3a;
  --green:#2aa043;
  --green-light:#7cbc2a;
  --ink:#2b2b2b;
  --muted:#8a8a8a;
  --faint:#eef4ea;
  --charcoal:#2e2e2e;
  --black:#050505;
  --white:#ffffff;
}
*{box-sizing:border-box;margin:0;padding:0}
html,body{width:1200px;height:3000px;overflow:hidden;background:var(--white)}
body{font-family:"Roboto",sans-serif;color:var(--ink)}
.page{position:absolute;left:268px;top:122px;width:664px;height:2755px;overflow:hidden;background:var(--white);box-shadow:0 0 14px rgba(0,0,0,.08)}
.abs{position:absolute}
.head{font-family:"Barlow Condensed",sans-serif;font-weight:600;line-height:1}
.small{font-family:"Roboto",sans-serif;font-size:6.6px;line-height:9.4px;color:var(--muted)}

/* hero */
.hero{left:0;top:0;width:664px;height:373px;overflow:hidden}
.hero-photo{position:absolute;left:120px;top:0;width:544px;height:373px;background:linear-gradient(90deg,#ffffff 0%,#eef0ef 22%,#d9dcdb 55%,#c9cccb 100%);border-bottom-left-radius:260px 80px}
.brand{display:flex;align-items:center;gap:6px}
.brand-dot{width:22px;height:22px;border-radius:50%;background:var(--green)}
.brand-name{font-family:"Barlow Condensed",sans-serif;font-weight:600;font-size:14px;color:var(--green-dark)}
.nav{right:45px;top:18px;display:flex;gap:12px;align-items:center;font-size:8px;color:#666}
.lang{background:var(--green);color:#fff;border-radius:8px;padding:2px 8px;font-size:7px}
.hero-title{left:68px;top:137px;font-size:33px;color:var(--green-light)}
.hero-tag{left:71px;top:184px;font-family:"Montserrat",sans-serif;font-size:13px;letter-spacing:4.2px;color:#666}
.hero-copy{left:72px;top:224px;font-family:"Montserrat",sans-serif;font-size:16px;line-height:21px;color:#333}
.btn{display:inline-block;background:var(--green);color:#fff;border-radius:12px;font-family:"Montserrat",sans-serif;font-weight:600}
.hero-btn{left:72px;top:278px;font-size:8px;padding:3px 9px}
.arrow{top:180px;font-size:22px;color:var(--green);font-family:"Montserrat",sans-serif}
.dots{left:289px;top:358px;display:flex;gap:5px}
.dots span{width:12px;height:2px;background:#fff}
.dots span:first-child{background:var(--green)}
.bush{left:440px;top:270px;width:230px;height:228px;border-radius:50%;background:radial-gradient(circle at 40% 35%,#5fae3a,#2f7d25 60%,#1e5a1a)}

/* about */
.bignum{font-family:"Barlow Condensed",sans-serif;font-size:50px;color:#ececec;line-height:1}
.about-title{font-size:28px;color:var(--green)}
.about-title.light{color:var(--green-light)}
.center{text-align:center}

/* band */
.band{left:0;top:769px;width:664px;height:341px;border-top-right-radius:150px;background:linear-gradient(90deg,#25963f,#2ea748 60%,#3fb058)}
.band-title{left:62px;top:800px;font-size:29px;color:#fff;font-weight:500}
.band-sub{font-family:"Roboto",sans-serif;font-weight:500;font-size:11px;color:#fff}
.band-list{list-style:none;font-size:8.8px;color:#fff;line-height:15.7px}
.band-list li::before{content:"";display:inline-block;width:4px;height:4px;border-radius:50%;background:#fff;margin-right:7px;vertical-align:middle}
.divider{left:331px;top:870px;height:132px;border-left:1.5px dashed #fff}
.van{left:33px;top:1030px;width:311px;height:168px;border-radius:40px 70px 26px 26px;background:linear-gradient(180deg,#f5f5f5,#d8d8d8 70%,#555 100%)}

/* services */
.tree-decor{left:440px;top:1180px;width:240px;height:500px;border-radius:50% 50% 20% 20%;background:radial-gradient(ellipse at 50% 30%,rgba(124,188,42,.16),rgba(124,188,42,.05) 60%,rgba(255,255,255,0) 75%)}
.services-title{left:0;width:664px;top:1240px;font-size:31px;color:var(--green);font-weight:500}
.services-intro{left:66px;width:532px;top:1300px;font-size:8px;line-height:11px;color:var(--muted)}
.card{width:248px;height:137px;background:#fff;border-radius:14px;box-shadow:0 3px 12px rgba(0,0,0,.12)}
.card h3{position:absolute;top:48px;font-family:"Barlow Condensed",sans-serif;font-weight:600;font-size:15px;color:var(--green)}
.card p{position:absolute;top:76px;font-size:7.4px;line-height:10px;color:#9a9a9a}
.card.left h3,.card.left p{right:18px;text-align:right}
.card.right h3,.card.right p{left:22px}
.card p{width:210px}
.icon{width:62px;height:62px;border-radius:50%;background:var(--green);display:flex;align-items:center;justify-content:center;box-shadow:0 2px 6px rgba(0,0,0,.2)}

/* contact band */
.dark{left:0;top:1724px;width:664px;height:195px;background:linear-gradient(90deg,#3a3a3a,#262626)}
.boxes{left:47px;top:1689px;width:174px;height:227px;border-radius:28px 28px 8px 8px;background:linear-gradient(160deg,#e6dcc6,#c9ae7c 60%,#a88b58)}
.dark-title{left:310px;top:1768px;font-size:23px;color:#fff;font-weight:500}
.dark-title em{font-style:normal;color:var(--green-light)}
.dark-copy{left:308px;top:1813px;width:288px;font-size:6.4px;line-height:8.2px;color:#e6e6e6}
.dark-btn{left:401px;top:1872px;font-size:8px;padding:4px 12px;background:var(--green-light)}

/* careers */
.careers-title{left:0;width:664px;top:1960px;font-size:34px;color:var(--green);font-weight:500}
.careers-copy{left:36px;top:2019px;width:296px;font-family:"Montserrat",sans-serif;font-size:8px;line-height:15.6px;color:#444}
.read-btn{left:36px;top:2200px;font-size:11px;padding:4px 24px}
.acc{left:349px;width:286px;border-top:1.5px solid #ddd;font-family:"Montserrat",sans-serif;font-size:8.4px;color:var(--green);font-weight:500}
.acc span.sign{display:inline-block;width:22px;font-size:13px}
.tasks{left:372px;top:2092px;width:270px;font-size:5.6px;line-height:10.4px;color:#666;list-style:none}

/* contact */
.contact-title{left:42px;top:2282px;font-size:33px;color:var(--green)}
.contact-title em{font-style:normal;color:var(--green-light)}
.info-label{font-family:"Montserrat",sans-serif;font-size:10.5px;color:#333}
.info-value{font-size:7px;color:#777;margin-top:3px}
.field{border:1px solid #ddd;border-radius:2px;font-size:6.6px;color:#999;padding:5px 7px}
.send{left:269px;top:2499px;font-size:12px;padding:5px 15px;font-weight:500}

/* footer */
.footer{left:0;top:2569px;width:664px;height:169px;background:var(--black)}
.footer-brand .brand-dot{width:34px;height:34px}
.footer-brand .brand-name{font-size:21px;color:var(--green)}
.social{display:flex;gap:12px}
.social span{width:24px;height:24px;border-radius:50%;background:var(--green)}
.footer-nav{display:flex;gap:18px;font-family:"Montserrat",sans-serif;font-size:11px;color:#fff}
.copyright{left:0;top:2738px;width:664px;height:17px;background:var(--green);color:#fff;font-family:"Montserrat",sans-serif;font-size:9.5px;line-height:17px;text-align:center;letter-spacing:.4px}
</style>
</head>
<body>
<div class="page">

  <!-- hero -->
  <section class="abs hero">
    <div class="hero-photo" role="img" aria-label="Photo of a delivery driver in a face mask climbing into an electric van"></div>
    <div class="abs brand" style="left:32px;top:12px"><span class="brand-dot"></span><span class="brand-name">BROOK LOGISTICS</span></div>
    <nav class="abs nav"><span>Home</span><span>About</span><span>Services</span><span>Contact us</span><span class="lang">English ⌄</span></nav>
    <div class="abs arrow" style="left:22px">‹</div>
    <div class="abs arrow" style="left:635px">›</div>
    <h1 class="abs head hero-title">BROOK LOGISTICS</h1>
    <div class="abs hero-tag">Sustainable Last Mile</div>
    <p class="abs hero-copy">Because we care<br>about trees!</p>
    <span class="abs btn hero-btn">Get Started</span>
    <div class="abs dots"><span></span><span></span><span></span><span></span><span></span><span></span></div>
  </section>
  <div class="abs bush" role="img" aria-label="Photo of a round green shrub"></div>

  <!-- about -->
  <svg class="abs" style="left:0;top:400px" width="664" height="400" viewBox="0 0 664 400" fill="none" stroke="#555" stroke-width="1" stroke-dasharray="3 3">
    <path d="M228 70 C270 40 330 30 360 60 C390 90 380 130 420 150 C470 170 540 150 540 190"/>
    <path d="M200 360 C240 345 280 345 310 370 C330 390 360 400 390 380"/>
  </svg>
  <div class="abs bignum" style="left:50px;top:432px">01</div>
  <h2 class="abs head about-title" style="left:70px;top:448px">Who We Are</h2>
  <p class="abs small center" style="left:56px;top:500px;width:270px">Brook Logistics is a pioneer in urban green logistics and provides zero-emissions last mile delivery services for its logistics and retail clients. We take on urban parcel delivery for our clients with a 100% electric commercial vehicles fleet, fair and sustainable working conditions for our employees and an unparalleled professional and customer-focused mindset.</p>
  <div class="abs bignum" style="left:358px;top:547px">02</div>
  <h2 class="abs head about-title light" style="left:376px;top:561px">Our Mission</h2>
  <p class="abs small center" style="left:362px;top:613px;width:270px">To satisfy consumers' ever-rising desire to buy products online, the CO2 emissions from delivery traffic will increase by 32% in the top 100 cities globally until 2030. Our clients care about our planet the same way we do, which is why Brook Logistics helps to make the planet a better place by running the most environmentally friendly urban last mile possible.</p>
  <div class="abs bignum" style="left:42px;top:614px">03</div>
  <h2 class="abs head about-title light" style="left:62px;top:628px">Our Values</h2>
  <p class="abs small center" style="left:49px;top:680px;width:270px">We see ourselves as a Professionalservices company who strongly cares about the environment, its clients and their customers, as well as its employees. We believe that delivering parcels with zero emissions and providing a unique customer experience through a highly professional attitude and a great team spirit are the cornerstones for Brook Logistics to operate in today's world in a sustainable yet profitable way.</p>

  <!-- comparison band -->
  <section class="abs band" role="img" aria-label="Green tinted photo of a smiling delivery worker holding parcels"></section>
  <h2 class="abs head band-title">Brook Logistics is</h2>
  <div class="abs band-sub" style="left:62px;top:868px">An Ordinary Parcel Delivery Firm</div>
  <ul class="abs band-list" style="left:62px;top:905px">
    <li>Polluting our cities</li><li>Short-term oriented</li><li>Short-term oriented</li><li>Focusing on profit only</li><li>Yet another parcel delivery firm</li>
  </ul>
  <div class="abs divider"></div>
  <div class="abs band-sub" style="left:383px;top:871px">A pioneering Green Last Mile</div>
  <ul class="abs band-list" style="left:383px;top:906px">
    <li>Delivering parcels emissions-free</li><li>Putting customer experience first</li><li>Operating the business sustainably</li><li>Focusing on the environment, customers and employees</li><li>A professional services company</li>
  </ul>
  <div class="abs van" role="img" aria-label="Photo of a white electric delivery van with the company name on its side"></div>

  <!-- services -->
  <div class="abs tree-decor" role="img" aria-label="Faint illustration of a leafy tree with roots"></div>
  <h2 class="abs head services-title center">Our Services</h2>
  <p class="abs services-intro center">Brook Logistics provides last mile delivery services in urban areas to clients in the logistics and retail space. Our permanent employees are all highly trained and commit to highest professional standards which we continuously review and further develop with them.</p>

  <div class="abs card left" style="left:66px;top:1357px"><h3>Zero-emission delivery</h3><p>We operate a 100% electric commercial vehicle fleet</p></div>
  <div class="abs card right" style="left:349px;top:1357px"><h3>Highly trained delivery drivers</h3><p>We only employ permanently, train far above average, and live a great team spirit</p></div>
  <div class="abs card left" style="left:66px;top:1530px"><h3>Professional all around</h3><p>We honor our commitments and hold ourselves to the highest professional standards</p></div>
  <div class="abs card right" style="left:349px;top:1530px"><h3>Unparalleled customer focus</h3><p>We live a customer-oriented mindset, always measuring ourselves against their experience</p></div>

  <div class="abs icon" style="left:58px;top:1352px"><svg width="32" height="32" viewBox="0 0 32 32" fill="none" stroke="#fff" stroke-width="2"><circle cx="14" cy="18" r="10"/><path d="M9 20h10M10 20l2-5h4l2 5"/><path d="M22 8l5-5"/></svg></div>
  <div class="abs icon" style="left:558px;top:1352px"><svg width="32" height="32" viewBox="0 0 32 32" fill="none" stroke="#fff" stroke-width="2"><rect x="6" y="5" width="20" height="20" rx="3"/><path d="M6 15h20M10 9h12"/><circle cx="11" cy="20" r="1.5"/><circle cx="21" cy="20" r="1.5"/><path d="M9 25v3M23 25v3"/></svg></div>
  <div class="abs icon" style="left:58px;top:1524px"><svg width="32" height="32" viewBox="0 0 32 32" fill="none" stroke="#fff" stroke-width="2"><path d="M6 16a10 10 0 0 1 17-7l3-3v8h-8l3-3"/><path d="M26 16a10 10 0 0 1-17 7l-3 3v-8h8l-3 3"/><circle cx="16" cy="16" r="3"/></svg></div>
  <div class="abs icon" style="left:558px;top:1524px"><svg width="32" height="32" viewBox="0 0 32 32" fill="none" stroke="#fff" stroke-width="2.4"><circle cx="13" cy="13" r="8"/><path d="M19 19l8 8"/></svg></div>

  <!-- get in touch -->
  <section class="abs dark" role="img" aria-label="Dark photo of a handshake"></section>
  <div class="abs boxes" role="img" aria-label="Photo of a delivery worker carrying two cardboard parcels"></div>
  <h2 class="abs head dark-title"><em>Get in touch</em> with Brook Logistics</h2>
  <p class="abs dark-copy">We see ourselves as a Professionalservices company who strongly cares about the environment, its clients and their customers, as well as its employees. We believe that delivering parcels with zero emissions and providing a unique customer experience through a highly professional attitude and a great team spirit are the cornerstones for Brook Logistics to operate in today's world in a sustainable yet profitable way.</p>
  <span class="abs btn dark-btn">CONTACT US</span>

  <!-- careers -->
  <h2 class="abs head careers-title center">Careers</h2>
  <p class="abs careers-copy">If you join Brook Logistics, you join a family. We elevate one another, care for each other's wellbeing and growth, and celebrate our successes. We strongly believe growth is a team sport and that every member of the family fully contributes to the achievements of the company overall.<br>At the heart of everything we do at Brook Logistics is a relentless focus on our mission. That's why we aim to ensure our employees can follow their own passion at the workplace, be this working in a truly collaborative and caring team, putting a smile on a customer's face or making the world a better place.</p>
  <span class="abs btn read-btn">Read More &gt;&gt;</span>

  <div class="abs acc" style="top:2019px;padding-top:9px"><span class="sign">+</span>Full-time driver / parcel deliverer (m/f/d) for Berlin</div>
  <div class="abs acc" style="top:2045px;border-top:none;padding-top:8px"><span class="sign">−</span>Your tasks as a delivery driver:</div>
  <ul class="abs tasks">
    <li>- Delivery of packages to end customers</li>
    <li>- In the delivery center: preparation of the tour and loading of the delivery van with parcels</li>
    <li>- Drive from the delivery center to the delivery area - you will be guided by a navigation system</li>
    <li>- Delivery of the parcels to end customers in the delivery area - the navigation helps you here too</li>
    <li>- Suggest ideas for improvement in the delivery process</li>
    <li>- Take care of and charge the delivery van</li>
  </ul>
  <div class="abs acc" style="top:2156px;padding-top:9px"><span class="sign">+</span>Required knowledge and skills:</div>
  <div class="abs acc" style="top:2190px;padding-top:9px;border-bottom:1.5px solid #ddd;padding-bottom:9px"><span class="sign">+</span>What you can expected from the Brook Logistics family:</div>

  <!-- contact -->
  <h2 class="abs head contact-title">Contact <em>Us</em></h2>
  <svg class="abs" style="left:50px;top:2353px" width="14" height="120" viewBox="0 0 14 120" fill="none" stroke="var(--green)" stroke-width="1.4">
    <path d="M7 14s5-5 5-8.5a5 5 0 0 0-10 0C2 9 7 14 7 14z"/><circle cx="7" cy="5.5" r="1.6"/>
    <rect x="1" y="50" width="12" height="9"/><path d="M1 50l6 5 6-5"/>
    <path d="M2 95c1 5 5 9 10 10l1.5-2.5-3-2-1.5 1.5c-2-1-3.5-2.5-4.5-4.5L6 96l-2-3z"/>
  </svg>
  <div class="abs" style="left:78px;top:2352px"><div class="info-label">Location:</div><div class="info-value">12 Alder Street, Greenford, GF 53502</div></div>
  <div class="abs" style="left:78px;top:2399px"><div class="info-label">Email:</div><div class="info-value">hello@brooklogistics.example</div></div>
  <div class="abs" style="left:78px;top:2445px"><div class="info-label">Call:</div><div class="info-value">0900 555 0142</div></div>

  <div class="abs field" style="left:240px;top:2353px;width:181px;height:21px">Your Name</div>
  <div class="abs field" style="left:426px;top:2353px;width:182px;height:21px">Your Email</div>
  <div class="abs field" style="left:240px;top:2388px;width:368px;height:21px">Subject</div>
  <div class="abs field" style="left:240px;top:2422px;width:368px;height:62px">Message</div>
  <span class="abs btn send">Send Message</span>

  <!-- footer -->
  <footer class="abs footer"></footer>
  <div class="abs brand footer-brand" style="left:0;width:664px;justify-content:center;top:2594px"><span class="brand-dot"></span><span class="brand-name">BROOK LOGISTICS</span></div>
  <div class="abs social" style="left:0;width:664px;justify-content:center;top:2661px"><span></span><span></span><span></span><span></span></div>
  <nav class="abs footer-nav" style="left:0;width:664px;justify-content:center;top:2707px"><span>Home</span><span>About</span><span>Services</span><span>Contact us</span></nav>
  <div class="abs copyright">© 2020 Brook logistics  All Rights Reserved.</div>
</div>
</body>
</html>
```